Fixed price car insurance banner ad for insurance broker

We need a banner ad for addition to web pages and which will advertise an innovative insurance product we are selling.

We are an insurance broker and our product is a fixed price car insurance product.

The banner ad needs to display the company logo. This will be uploaded within the file upload section.

The remainder of the banner ad needs to explain what we are offering and also include the gear stick picture for impact.

We would like to see colours that tie in with the corporate colours, or alternative are striking and have presence on even the busiest web page I.e. Black banner and silver / white text. Please see the file upload for a sample of the brochure we are preparing for this product.

Target Market(s)

Private and commercial clients with both regular and high value motor vehicles.

Industry/Entity Type

Car Insurance

Font styles to use
Serif
Sans Serif

Colors

Designer to choose colors to be used in the design.

Requirements
Must have
• The banner must have the company logo on both pages.

I would like the advert to scroll / roll / fade or other between two pages displaying the following text:

Page 1
"Motor Insurance Scheme"
"Anything But Standard"
and including the gear knob picture

Page 2
Any Driver, Any Car, No Forms and One Flat Premium*

On clicking the banner ad, this will open an email, pre populated with email contact to request more detail.

Nice to have
• Open to your suggestions on this
Should not have
• Nothing at this stage. I will guide you when the ads are being submitted.

```html
<!DOCTYPE html>
<html lang="en">
<head>
<meta charset="utf-8">
<title>RDV Insurance – Motor Scheme Banners</title>
<link rel="stylesheet" href="https://fonts.googleapis.com/css2?family=Open+Sans:wght@300;400;600&display=swap">
<style>
  :root{
    --page:#ffffff;
    --frame:#1b1b1b;
    --panel:#2a2a2a;
    --panel-deep:#1f1f1f;
    --band:#050505;
    --cta-bg:#e9e9e9;
    --logo-bg:#ffffff;
    --logo-ink:#1d2b57;
    --text-light:#ffffff;
    --text-soft:#e4e4e4;
    --cta-ink:#111111;
  }
  html,body{margin:0;padding:0;width:1200px;height:1019px;overflow:hidden;background:var(--page);}
  body{font-family:"Open Sans",Arial,sans-serif;position:relative;}

  .banner{
    position:absolute;
    width:calc(727 * var(--u));
    height:calc(90 * var(--u));
    background:linear-gradient(180deg,var(--panel),var(--panel-deep));
    overflow:hidden;
  }
  .banner--large{--u:1.451px;left:90px;}
  .banner--small{--u:0.932px;left:91px;}
  .banner__shapes{position:absolute;inset:0;width:100%;height:100%;display:block;}

  .line{
    position:absolute;
    white-space:nowrap;
    line-height:1;
    transform:translateY(-50%);
  }

  .brand{
    left:calc(73 * var(--u));top:calc(45 * var(--u));
    transform:translate(-50%,-50%);
    color:var(--logo-ink);font-weight:600;
    font-size:calc(14 * var(--u));letter-spacing:calc(0.6 * var(--u));
  }

  .headline{left:calc(194 * var(--u));top:calc(31 * var(--u));font-size:calc(21 * var(--u));font-weight:600;color:var(--text-light);}
  .subline{left:calc(235 * var(--u));top:calc(59 * var(--u));font-size:calc(15 * var(--u));color:var(--text-soft);}

  .offer{font-size:calc(17 * var(--u));font-weight:600;color:var(--text-light);}
  .offer--first{left:calc(206 * var(--u));top:calc(32 * var(--u));}
  .offer--second{left:calc(258 * var(--u));top:calc(54 * var(--u));}

  .contact{font-size:calc(18 * var(--u));font-weight:300;color:var(--text-soft);}
  .contact strong{font-weight:600;color:var(--text-light);}
  .contact--email{left:calc(189 * var(--u));top:calc(31 * var(--u));}
  .contact--phone{left:calc(246 * var(--u));top:calc(55 * var(--u));}

  .gear-knob{
    position:absolute;
    left:calc(523 * var(--u));top:calc(6 * var(--u));
    width:calc(74 * var(--u));height:calc(74 * var(--u));
    border-radius:50%;
    background:radial-gradient(circle at 45% 40%,#fafafa 0%,#d8d8d8 40%,#a0a0a0 62%,#2a2a2a 68%,#0c0c0c 100%);
  }

  .cta{
    left:calc(631 * var(--u));top:calc(55 * var(--u));
    font-size:calc(16 * var(--u));color:var(--cta-ink);
    text-decoration:underline;text-underline-offset:calc(3 * var(--u));
  }
</style>
</head>
<body>

<svg width="0" height="0" style="position:absolute" aria-hidden="true">
  <defs>
    <g id="banner-shapes">
      <polygon points="3,3 143,3 173,45 143,87 3,87" fill="#ffffff"/>
      <polygon points="518,3 645,3 597,87 476,87" fill="#050505"/>
      <polygon points="645,3 724,3 724,87 597,87" fill="#e9e9e9"/>
      <rect x="1.5" y="1.5" width="724" height="87" fill="none" stroke="#1b1b1b" stroke-width="3"/>
    </g>
  </defs>
</svg>

<!-- Large set -->
<div class="banner banner--large" style="top:70px">
  <svg class="banner__shapes" viewBox="0 0 727 90" preserveAspectRatio="none" aria-hidden="true"><use href="#banner-shapes"/></svg>
  <div class="line brand">RDV INSURANCE</div>
  <div class="line headline">A Motor Insurance Scheme</div>
  <div class="line subline">- That's anything but standard</div>
  <div class="gear-knob" role="img" aria-label="Chrome gear knob photo with shift pattern"></div>
  <span class="line cta">learn more</span>
</div>

<div class="banner banner--large" style="top:222px">
  <svg class="banner__shapes" viewBox="0 0 727 90" preserveAspectRatio="none" aria-hidden="true"><use href="#banner-shapes"/></svg>
  <div class="line brand">RDV INSURANCE</div>
  <div class="line offer offer--first">Any Driver, Any Car, No Forms</div>
  <div class="line offer offer--second">and One Flat Premium</div>
  <div class="gear-knob" role="img" aria-label="Chrome gear knob photo with shift pattern"></div>
  <span class="line cta">learn more</span>
</div>

<div class="banner banner--large" style="top:377px">
  <svg class="banner__shapes" viewBox="0 0 727 90" preserveAspectRatio="none" aria-hidden="true"><use href="#banner-shapes"/></svg>
  <div class="line brand">RDV INSURANCE</div>
  <div class="line contact contact--email">email: <strong>dan.hollis@rdvins.co.uk</strong></div>
  <div class="line contact contact--phone">phone: <strong>07700 900462</strong></div>
  <div class="gear-knob" role="img" aria-label="Chrome gear knob photo with shift pattern"></div>
  <span class="line cta">learn more</span>
</div>

<!-- Small set -->
<div class="banner banner--small" style="top:622px">
  <svg class="banner__shapes" viewBox="0 0 727 90" preserveAspectRatio="none" aria-hidden="true"><use href="#banner-shapes"/></svg>
  <div class="line brand">RDV INSURANCE</div>
  <div class="line headline">A Motor Insurance Scheme</div>
  <div class="line subline">- That's anything but standard</div>
  <div class="gear-knob" role="img" aria-label="Chrome gear knob photo with shift pattern"></div>
  <span class="line cta">learn more</span>
</div>

<div class="banner banner--small" style="top:736px">
  <svg class="banner__shapes" viewBox="0 0 727 90" preserveAspectRatio="none" aria-hidden="true"><use href="#banner-shapes"/></svg>
  <div class="line brand">RDV INSURANCE</div>
  <div class="line offer offer--first">Any Driver, Any Car, No Forms</div>
  <div class="line offer offer--second">and One Flat Premium</div>
  <div class="gear-knob" role="img" aria-label="Chrome gear knob photo with shift pattern"></div>
  <span class="line cta">learn more</span>
</div>

<div class="banner banner--small" style="top:850px">
  <svg class="banner__shapes" viewBox="0 0 727 90" preserveAspectRatio="none" aria-hidden="true"><use href="#banner-shapes"/></svg>
  <div class="line brand">RDV INSURANCE</div>
  <div class="line contact contact--email">email: <strong>dan.hollis@rdvins.co.uk</strong></div>
  <div class="line contact contact--phone">phone: <strong>07700 900462</strong></div>
  <div class="gear-knob" role="img" aria-label="Chrome gear knob photo with shift pattern"></div>
  <span class="line cta">learn more</span>
</div>

</body>
</html>
```